Quenby Ballet Poster

We need a poster to illustrate a classical ballet on in 4 weeks.
It is a "white ballet".
Set in a forest glade.
Poster could feature one dancer or a couple.
Refer to our facebook page for more information:
https://www.pagelounge.example/quenbyballet
Target Market(s)
dance lovers, mature appreciators of classical ballet
Requirements
Must have
- long white tutu on a female dancer (one or more, or a couple)
Name of the ballet: "Les Vermeilles"
Place & Dates of performance: Tindale Theatre 19th & 20th July
"Quenby Ballet"

```html
<!DOCTYPE html>
<html lang="en">
<head>
<meta charset="UTF-8">
<title>Les Vermeilles – Quenby Ballet</title>
<link href="https://fonts.googleapis.com/css2?family=Pinyon+Script&family=Titillium+Web:wght@300&display=swap" rel="stylesheet">
<style>
  :root {
    --ink: #000000;
    --paper: #ffffff;
    --band-light: #b4b4b4;
    --band-mid: #6e6e6e;
    --stage-glow: #c9d3e6;
    --stage-mid: #5d6a85;
    --stage-floor: #2a3140;
  }
  * { margin: 0; padding: 0; box-sizing: border-box; }
  html, body {
    width: 849px;
    height: 1200px;
    overflow: hidden;
    background: var(--ink);
  }
  .poster {
    position: relative;
    width: 849px;
    height: 1200px;
    background: var(--ink);
    color: var(--paper);
    font-family: "Titillium Web", sans-serif;
    font-weight: 300;
  }
  .ballet-title {
    position: absolute;
    top: 70px;
    left: 0;
    width: 100%;
    text-align: center;
    font-family: "Pinyon Script", cursive;
    font-weight: 400;
    font-size: 132px;
    line-height: 1.3;
    letter-spacing: 2px;
  }
  .band {
    position: absolute;
    left: 0;
    width: 849px;
    text-align: center;
    font-size: 54px;
    line-height: 1.15;
  }
  .band--company {
    top: 380px;
    height: 83px;
    padding-top: 8px;
    background: linear-gradient(to right, var(--band-light) 0%, var(--band-mid) 35%, var(--ink) 100%);
  }
  .band--details {
    top: 518px;
    height: 138px;
    padding-top: 10px;
    background: linear-gradient(to right, var(--ink) 0%, var(--band-mid) 55%, var(--band-light) 100%);
  }
  .stage-photo {
    position: absolute;
    left: 0;
    top: 760px;
    width: 849px;
    height: 440px;
    background:
      radial-gradient(ellipse 60% 45% at 48% 50%, var(--stage-glow) 0%, var(--stage-mid) 55%, transparent 80%),
      linear-gradient(to bottom, var(--ink) 0%, var(--ink) 15%, var(--stage-floor) 82%, var(--ink) 100%);
  }
</style>
</head>
<body>
  <main class="poster">
    <h1 class="ballet-title">Les Vermeilles</h1>
    <div class="band band--company">Quenby Ballet</div>
    <div class="band band--details">July 19–20<br>Tindale Theatre</div>
    <div class="stage-photo" role="img" aria-label="Photograph of a line of ballerinas in long white romantic tutus dancing on pointe on a dark stage, seen from behind"></div>
  </main>
</body>
</html>
```